Identification Supplier website

Front and product page designs required for this Business Catalyst website for an identification supply company.

Also interested in coding same into finished site for additional fee.

Client is a security/event ID supplies company selling identification products like card holders, printers, lanyards, clips and so on.

Current placeholder site is at:
http://www.tagmorrow.com.au/

Other sites the client likes are at:

www.varrowdesigns.com.au

www.badgenook.com.au

www.qrv.com.au

http://start42.brimfield.co.nz/online/welcome.csn

Otherwise colour scheme should follow logo and structure should follow wireframe attached.

Industry/Entity Type

Business

```html
<!DOCTYPE html>
<html lang="en">
<head>
<meta charset="utf-8">
<title>Tagmorrow – ID Supplies</title>
<link href="https://fonts.googleapis.com/css2?family=Arimo:wght@400;700&family=Signika:wght@500;600&display=swap" rel="stylesheet">
<style>
:root{
  --blue:#0a86c6;
  --blue-dark:#0b5c93;
  --navy:#173a62;
  --orange:#ee8a00;
  --text:#444;
  --line:#d9dfe5;
  --page:#e6ecf1;
  --white:#fff;
}
*{box-sizing:border-box;margin:0;padding:0}
html,body{width:1200px;height:957px;overflow:hidden}
body{position:relative;background:linear-gradient(180deg,#e9eff4 0%,#dfe7ee 60%,#e8eef3 100%);font-family:"Arimo",Arial,sans-serif;color:var(--text)}
.abs{position:absolute}

.topbar{left:0;top:0;width:1200px;height:35px;background:var(--blue)}
.topbar .contact{left:808px;top:10px;color:var(--white);font-size:11px;display:flex;align-items:center;gap:8px}
.social{display:flex;gap:3px;margin-left:10px}
.social span{width:16px;height:16px;border-radius:50%;background:#f1f4f7;display:block}

.logo{left:162px;top:54px;display:flex;align-items:center;gap:8px}
.logo .dot{width:22px;height:22px;border-radius:50%;background:var(--blue)}
.logo .name{font-family:"Signika",Arial,sans-serif;font-weight:500;font-size:31px;color:var(--navy);letter-spacing:.5px}

.nav{top:69px;height:26px;font-family:"Signika",Arial,sans-serif;font-weight:600;font-size:13px;color:var(--navy);line-height:26px;white-space:nowrap}
.nav.active{background:var(--orange);color:var(--white);width:60px;text-align:center}
.rule{left:161px;top:105px;width:878px;height:2px;background:var(--blue)}

.slider{left:161px;top:111px;width:651px;height:223px;background:linear-gradient(135deg,#1f8fd0 0%,#0f6eb4 60%,#0b5ea0 100%)}
.slider .art{left:90px;top:40px;width:320px;height:150px;border-radius:6px;background:linear-gradient(180deg,#f6a623,#ef8a10)}
.slider .tagline{right:18px;bottom:12px;font-family:"Signika",Arial,sans-serif;font-size:21px;color:var(--white);white-space:nowrap}
.slider .tagline em{font-style:normal;color:var(--orange)}
.dots{left:14px;bottom:12px;display:flex;gap:4px}
.dots span{width:10px;height:10px;border-radius:50%;background:var(--white)}
.dots span.on{background:var(--orange)}

.news{left:820px;top:111px;width:219px;height:223px;background:var(--white);border:1px solid var(--line)}
.news .head{height:36px;border-bottom:1px solid var(--line);display:flex;align-items:center;padding-left:22px;gap:6px;font-family:"Signika",Arial,sans-serif;font-weight:600;font-size:11px;color:var(--navy)}
.news .item{padding:8px 8px 0 16px}
.news h4{font-weight:400;font-size:11.5px;color:#333;margin-bottom:4px}
.news p{font-size:9.3px;line-height:15px;color:#555}
.news hr{border:0;border-top:1px solid var(--line);margin:5px 6px 0 0}

.panel{left:161px;top:347px;width:878px;height:531px;background:var(--white);border:1px solid var(--line)}
.heading{display:flex;align-items:center;gap:6px;font-family:"Signika",Arial,sans-serif;font-weight:600;font-size:13px;color:var(--navy);border-bottom:1px solid var(--line);padding-bottom:4px;white-space:nowrap}
.heading .mark{width:21px;height:21px;background:var(--orange);display:flex;align-items:center;justify-content:center}
.intro{left:171px;top:390px;width:625px;font-size:10.4px;line-height:16.7px;color:#444;text-align:justify}
.btn{background:var(--blue-dark);color:var(--white);font-size:10.5px;height:23px;line-height:23px;padding:0 9px 0 6px;display:flex;gap:8px;align-items:center;white-space:nowrap}
.btn::after{content:"";border-left:5px solid #9cc6e6;border-top:4px solid transparent;border-bottom:4px solid transparent}

.product{width:305px;height:151px;border:1px solid var(--line);background:var(--white)}
.product h3{position:absolute;left:11px;top:15px;font-family:"Signika",Arial,sans-serif;font-weight:600;font-size:11px;color:var(--navy)}
.product .photo{position:absolute;left:11px;top:39px;width:95px;height:88px;border:1px solid #ddd}
.product p{position:absolute;left:120px;top:38px;width:166px;height:82px;overflow:hidden;font-size:9.8px;line-height:16.6px;text-align:justify;color:#555}
.product .more{position:absolute;right:20px;top:127px;font-size:9.5px;color:var(--blue-dark)}

.letter{left:808px;top:361px;width:222px;height:61px;background:var(--orange)}
.letter .label{left:15px;top:9px;font-family:"Signika",Arial,sans-serif;font-weight:600;font-size:11.5px;color:var(--white)}
.letter .field{left:14px;top:27px;width:154px;height:21px;background:var(--white);font-size:9px;color:#999;padding:5px 10px;white-space:nowrap}
.letter .go{left:168px;top:27px;width:36px;height:21px;background:var(--blue-dark);color:var(--white);font-size:9px;line-height:21px;padding-left:5px;white-space:nowrap}
.signup{left:808px;top:428px;width:222px;height:97px;background:linear-gradient(180deg,#1a86c9,#0e64a6);text-align:center;color:#e3eef8}
.signup .small{margin-top:26px;font-family:"Signika",Arial,sans-serif;font-weight:600;font-size:13px}
.signup .big{margin-top:4px;font-family:"Signika",Arial,sans-serif;font-weight:600;font-size:22px;color:var(--white)}
.signup .big em{font-style:normal;color:var(--orange)}
.featured{left:808px;top:532px;width:222px;height:35px;background:var(--navy);color:var(--white);font-family:"Signika",Arial,sans-serif;font-weight:600;font-size:12px;padding:10px 0 0 14px}
.arrows{right:8px;top:9px;display:flex;gap:4px}
.arrows span{width:18px;height:17px;background:var(--orange);display:flex;align-items:center;justify-content:center}
.feat-photo{left:808px;top:569px;width:222px;height:128px;border:2px solid var(--blue);background:linear-gradient(135deg,#f6e25a,#f2c530)}
.feat-text{left:810px;top:703px;width:218px;font-size:9.8px;line-height:16.6px;text-align:justify;color:#555}

.footer{left:0;top:889px;width:1200px;height:68px;background:var(--blue);color:var(--white);font-size:10.5px}
.footer .links{left:162px;top:13px;display:flex;gap:10px}
.footer .copy{right:161px;top:11px;white-space:nowrap}
</style>
</head>
<body>
<header class="abs topbar">
  <div class="abs contact">
    <svg width="13" height="13" viewBox="0 0 24 24" aria-hidden="true"><path fill="#fff" d="M6.6 10.8c1.4 2.8 3.8 5.1 6.6 6.6l2.2-2.2c.3-.3.7-.4 1-.2 1.1.4 2.3.6 3.6.6.6 0 1 .4 1 1V20c0 .6-.4 1-1 1C10.6 21 3 13.4 3 4c0-.6.4-1 1-1h3.5c.6 0 1 .4 1 1 0 1.3.2 2.5.6 3.6.1.3 0 .7-.2 1z"/></svg>
    <span>03-9000 4127</span><span>|</span><span>Follow us on</span>
    <span class="social"><span></span><span></span><span></span></span>
  </div>
</header>

<div class="abs logo"><span class="dot"></span><span class="name">tagmorrow</span></div>

<nav>
  <span class="abs nav active" style="left:625px">HOME</span>
  <span class="abs nav" style="left:690px">ABOUT US</span>
  <span class="abs nav" style="left:765px">PRODUCTS</span>
  <span class="abs nav" style="left:845px">SUPPORT</span>
  <span class="abs nav" style="left:917px">CONTACT US</span>
  <span class="abs nav" style="left:1006px">NEWS</span>
</nav>
<div class="abs rule"></div>

<section class="abs slider">
  <div class="abs art" role="img" aria-label="Printed orange ID card with a plastic card behind it"></div>
  <div class="abs dots"><span></span><span class="on"></span><span></span><span></span></div>
  <div class="abs tagline">Yes, <em>We</em> Mean <em>Everything</em>....</div>
</section>

<aside class="abs news">
  <div class="head">
    <svg width="16" height="18" viewBox="0 0 16 18" aria-hidden="true"><path d="M1 1h9l4 4v12H1z" fill="none" stroke="#0a86c6" stroke-width="2"/><path d="M9 10h6M12 7v6" stroke="#0a86c6" stroke-width="2"/></svg>
    WHAT'S NEW !
  </div>
  <div class="item">
    <h4>Lorem Ipsum</h4>
    <p>Lorem Ipsum is simply dummy text of the printing and typesetting industry. Lorem Ipsum has been the industry's standard dummy text ever since the 1500s,</p>
    <hr>
  </div>
  <div class="item">
    <h4>Lorem Ipsum</h4>
    <p>Lorem Ipsum is simply dummy text of the printing and typesetting industry. Lorem Ipsum has been the industry's standard dummy text ever since the 1500s,</p>
  </div>
</aside>

<main class="abs panel"></main>

<h2 class="abs heading" style="left:171px;top:355px;width:625px">
  <span class="mark"><svg width="8" height="10" viewBox="0 0 8 10"><path d="M0 0l8 5-8 5z" fill="#fff"/></svg></span>WHY TAGMORROW
</h2>
<div class="abs intro">
  <p>Yes, We mean everything.</p>
  <p>From membership cards...to the latest holographic effect ID badges for the most security sensitive organisations. And as the ID specialist we'll even help you with advice on the design and printing of your customised membership or ID cards as well as specifications to suit your budget.</p>
</div>
<a class="abs btn" style="left:171px;top:460px">ReadMore</a>

<h2 class="abs heading" style="left:171px;top:512px;width:625px">
  <span class="mark"><svg width="8" height="10" viewBox="0 0 8 10"><path d="M0 0l8 5-8 5z" fill="#fff"/></svg></span>EVERYTHING YOU WILL EVER NEED IN ID SUPPLIES....
</h2>

<article class="abs product" style="left:171px;top:550px">
  <h3>CARD PRINTERS</h3>
  <div class="photo" role="img" aria-label="Card printer ribbons and cartridges" style="background:linear-gradient(135deg,#dbe6f2,#2d5d9c)"></div>
  <p>Lorem Ipsum is simply dummy text of the printing and typesetting industry. Lorem Ipsum has been the industry's standard dummy text ever since the 1500s, when an unknown printer took</p>
  <span class="more">More...</span>
</article>
<article class="abs product" style="left:492px;top:550px">
  <h3>CARDHOLDERS</h3>
  <div class="photo" role="img" aria-label="Card holders in black, white and pink" style="background:linear-gradient(135deg,#555,#eee 55%,#f04a86)"></div>
  <p>Lorem Ipsum is simply dummy text of the printing and typesetting industry. Lorem Ipsum has been the industry's standard dummy text ever since the 1500s, when an unknown printer took</p>
  <span class="more">More...</span>
</article>
<article class="abs product" style="left:171px;top:712px">
  <h3>LANYARDS</h3>
  <div class="photo" role="img" aria-label="Assorted coloured lanyards" style="background:linear-gradient(135deg,#f5f5f5,#c9d4e0)"></div>
  <p>Lorem Ipsum is simply dummy text of the printing and typesetting industry. Lorem Ipsum has been the industry's standard dummy text ever since the 1500s, when an unknown printer took</p>
  <span class="more">More...</span>
</article>
<article class="abs product" style="left:492px;top:712px">
  <h3>WRISTBANDS</h3>
  <div class="photo" role="img" aria-label="Colourful silicone wristbands" style="background:linear-gradient(135deg,#e9e6ec,#c45ad0 50%,#f2d43a)"></div>
  <p>Lorem Ipsum is simply dummy text of the printing and typesetting industry. Lorem Ipsum has been the industry's standard dummy text ever since the 1500s, when an unknown printer took</p>
  <span class="more">More...</span>
</article>

<aside>
  <div class="abs letter">
    <span class="abs label">NEWS LETTER</span>
    <span class="abs field">Enter Your Mail ID....</span>
    <span class="abs go">GO ▸</span>
  </div>
  <div class="abs signup">
    <div class="small">Sign Up to Receive &nbsp;Our Free</div>
    <div class="big">NEWS <em>LETTER</em></div>
  </div>
  <div class="abs featured">FEATURED PRODUCT
    <span class="abs arrows">
      <span><svg width="6" height="8" viewBox="0 0 6 8"><path d="M6 0L0 4l6 4z" fill="#fff"/></svg></span>
      <span><svg width="6" height="8" viewBox="0 0 6 8"><path d="M0 0l6 4-6 4z" fill="#fff"/></svg></span>
    </span>
  </div>
  <div class="abs feat-photo" role="img" aria-label="Black and green business cards on a yellow background"></div>
  <p class="abs feat-text">Lorem Ipsum is simply dummy text of the printing and typesetting industry. Lorem Ipsum has been the industry's standard dummy text ever since the 1500s, when an unknown printer took a galley of type and scrambled it to make a type specimen book.</p>
  <a class="abs btn" style="left:812px;top:805px">Read More</a>
</aside>

<footer class="abs footer">
  <div class="abs links"><span>Home</span><span>|</span><span>About Us</span><span>|</span><span>Products</span><span>|</span><span>Support</span><span>|</span><span>Contact Us</span><span>|</span><span>News</span></div>
  <div class="abs copy">Copyright©tagmorrow.com.au. All Rights Reserved.</div>
</footer>
</body>
</html>
```